Summit Guest Partners

An Editable Business Card Template For SGP & SGH
Similar or Different Design

418 W. Marlow Ridge Pkwy.
Suite 2230
Irving, TX 75038

```html
<!DOCTYPE html>
<html lang="en">
<head>
<meta charset="utf-8">
<title>Summit Guest Partners – Business Card</title>
<link href="https://fonts.googleapis.com/css2?family=EB+Garamond:wght@500;600&family=Montserrat:wght@400;500&display=swap" rel="stylesheet">
<style>
  :root {
    --stage: #2b2b2d;
    --card-light: #f7f7f7;
    --card-dark: #0b0b0b;
    --brand-red: #a51d24;
    --brand-red-soft: #c9453f;
    --ink: #2a2a2a;
    --ink-light: #f2f2f2;
  }
  * { box-sizing: border-box; margin: 0; padding: 0; }
  html, body { width: 1200px; height: 900px; overflow: hidden; }
  body {
    background: var(--stage);
    font-family: "Montserrat", sans-serif;
    display: flex;
    align-items: center;
    justify-content: center;
    gap: 90px;
  }
  .card {
    width: 360px;
    height: 630px;
    border-radius: 30px;
    position: relative;
    display: flex;
    flex-direction: column;
    align-items: center;
    box-shadow: 0 18px 40px rgba(0,0,0,.45);
  }
  .card--front { background: var(--card-light); color: var(--ink); }
  .card--back { background: var(--card-dark); color: var(--ink-light); }

  .brand {
    margin-top: 70px;
    display: flex;
    align-items: center;
    gap: 14px;
  }
  .brand__dot {
    width: 44px; height: 44px; border-radius: 50%;
    background: var(--brand-red);
    flex: none;
  }
  .brand__name {
    font-family: "EB Garamond", serif;
    font-weight: 600;
    font-size: 30px;
    line-height: 1.05;
    color: var(--brand-red);
  }
  .card--back .brand__name { color: var(--brand-red-soft); }

  .person { margin-top: 150px; text-align: center; }
  .person__name {
    font-family: "EB Garamond", serif;
    font-weight: 600;
    font-size: 36px;
    color: var(--brand-red);
    line-height: 1;
  }
  .person__role { font-size: 15px; margin-top: 4px; }

  .divider {
    display: flex; align-items: center; gap: 8px;
    width: 290px; margin-top: 18px;
  }
  .divider__line { flex: 1; height: 1.5px; background: var(--brand-red); }
  .divider__icons { display: flex; gap: 4px; }
  .icon {
    width: 24px; height: 24px; border-radius: 5px;
    background: var(--brand-red);
    display: flex; align-items: center; justify-content: center;
  }
  .contact { margin-top: 16px; text-align: center; font-size: 16px; line-height: 1.45; }
  .rule { width: 120px; height: 1.5px; background: var(--brand-red); margin-top: 20px; }
  .address { margin-top: 16px; text-align: center; font-size: 16px; line-height: 1.45; }

  .services { margin-top: 110px; width: 290px; }
  .services__title {
    font-family: "EB Garamond", serif;
    font-weight: 600;
    font-size: 44px;
    color: var(--brand-red-soft);
    text-align: center;
    margin-bottom: 16px;
  }
  .services__list { list-style: none; font-size: 15px; line-height: 1.3; }
  .services__list li {
    position: relative;
    padding-left: 20px;
    margin-bottom: 14px;
  }
  .services__list li::before {
    content: "";
    position: absolute; left: 2px; top: 7px;
    width: 7px; height: 7px; border-radius: 50%;
    background: var(--brand-red-soft);
  }
</style>
</head>
<body>
  <article class="card card--front">
    <div class="brand">
      <span class="brand__dot"></span>
      <span class="brand__name">Summit Guest<br>Housing</span>
    </div>
    <div class="person">
      <h1 class="person__name">Dana Whitfield</h1>
      <p class="person__role">Sales Manager</p>
    </div>
    <div class="divider">
      <span class="divider__line"></span>
      <span class="divider__icons">
        <span class="icon" aria-label="Phone">
          <svg width="14" height="14" viewBox="0 0 24 24"><path fill="#fff" d="M6.6 10.8a15 15 0 0 0 6.6 6.6l2.2-2.2c.3-.3.7-.4 1-.2 1.1.4 2.3.6 3.6.6.6 0 1 .4 1 1V20c0 .6-.4 1-1 1A17 17 0 0 1 3 4c0-.6.4-1 1-1h3.5c.6 0 1 .4 1 1 0 1.3.2 2.5.6 3.6.1.3 0 .7-.2 1z"/></svg>
        </span>
        <span class="icon" aria-label="Email">
          <svg width="14" height="14" viewBox="0 0 24 24"><rect x="2" y="5" width="20" height="14" rx="1.5" fill="#fff"/><path d="M3 6l9 7 9-7" fill="none" stroke="#a51d24" stroke-width="1.8"/></svg>
        </span>
        <span class="icon" aria-label="Website">
          <svg width="14" height="14" viewBox="0 0 24 24"><circle cx="12" cy="12" r="9" fill="none" stroke="#fff" stroke-width="2"/><ellipse cx="12" cy="12" rx="4" ry="9" fill="none" stroke="#fff" stroke-width="1.6"/><path d="M3 12h18" stroke="#fff" stroke-width="1.6"/></svg>
        </span>
      </span>
      <span class="divider__line"></span>
    </div>
    <p class="contact">
      214.555.0147<br>
      dwhitfield@summitguest.com<br>
      www.sgpfield.com
    </p>
    <span class="rule"></span>
    <p class="address">
      418 W. Marlow Ridge Pkwy.<br>
      Suite 2230<br>
      Irving, TX 75038
    </p>
  </article>

  <article class="card card--back">
    <div class="brand">
      <span class="brand__dot"></span>
      <span class="brand__name">Summit Guest<br>Housing</span>
    </div>
    <section class="services">
      <h2 class="services__title">Services</h2>
      <ul class="services__list">
        <li>Proven Track Record Of Performance</li>
        <li>Live Customer Support 24/7/365</li>
        <li>Experienced Lodging Provider To Various Corporate Industries</li>
        <li>Consolidated Billing/Administration</li>
        <li>Full-Service Lodging Including Multiple Long-Term Options</li>
        <li>No Additional Fees</li>
      </ul>
    </section>
  </article>
</body>
</html>
```